Corporate Brightfen business cards to be handed to investor, bankers etc. Needs to have a young feel

I need business cards designed for a technology company that provides uber-like rapid response on the security industry. I would like it simple but very cool and tasteful. See attached documents for artwork and colours to be used. Cut sheet describes business model. Card stock should be thicker than normal. I would like the one side to be just the art and the other to have the contact info with maybe the pin somewhere.

Target Market(s)

Investors

Industry/Entity Type

Business

Contact Information for Business Card

Would like the logo attached on one side with name address and other info on the other side.

Font styles to use
Other font styles liked:
• See existing logo

Colors
6b449b
886aae
e4daeb
ffffff

Requirements
Must have
• Name: Dorian Felkatsis
• Address: 47 Larkfield Avenue, Toronto, On, M6K2B7
• Tel: 416-7291846
• Email: rolo@brightfen.io
Nice to have
• See logo colours

```html
<!DOCTYPE html>
<html lang="en">
<head>
<meta charset="utf-8">
<title>Brightfen Business Cards</title>
<link rel="stylesheet" href="https://fonts.googleapis.com/css2?family=Lato:wght@300;400;700&display=swap">
<style>
  :root {
    --brand-purple: #6b449b;
    --brand-lilac: #886aae;
    --brand-mist: #e4daeb;
    --brand-white: #ffffff;
    --ink: #1c1c1c;
    --stage: #1f1f21;
    --card-dark-top: #4a4a4c;
    --card-dark-bottom: #262628;
    --rule: #9a9a9a;
  }
  * { box-sizing: border-box; margin: 0; padding: 0; }
  html, body {
    width: 1200px;
    height: 873px;
    overflow: hidden;
    background: var(--stage);
    font-family: "Lato", Arial, sans-serif;
  }
  .stage {
    position: relative;
    width: 1200px;
    height: 873px;
  }
  .card {
    position: absolute;
    top: 281px;
    width: 540px;
    height: 310px;
    border-radius: 16px;
    overflow: hidden;
  }
  /* Art side */
  .card--art { left: 40px; }
  .card__backdrop {
    position: absolute;
    inset: 0;
    background: linear-gradient(160deg, var(--card-dark-top) 0%, #3a3a3c 45%, var(--card-dark-bottom) 100%);
  }
  .card__content {
    position: absolute;
    inset: 0;
    display: flex;
    flex-direction: column;
    align-items: center;
    justify-content: center;
    text-align: center;
    color: var(--brand-white);
    padding: 0 44px;
  }
  .wordmark {
    display: flex;
    align-items: center;
    gap: 8px;
    font-weight: 300;
    letter-spacing: -0.5px;
    line-height: 1;
    white-space: nowrap;
  }
  .wordmark__dot {
    border-radius: 50%;
    background: var(--brand-lilac);
    flex: none;
  }
  .card--art .wordmark { font-size: 50px; color: var(--brand-white); margin-bottom: 22px; }
  .card--art .wordmark__dot { width: 20px; height: 20px; margin-top: 10px; }
  .pitch {
    font-size: 11.5px;
    line-height: 1.45;
    font-weight: 400;
    color: #ececec;
  }
  .pitch__tagline {
    margin-top: 10px;
    font-size: 14px;
    font-weight: 700;
    letter-spacing: 0.2px;
  }
  .pitch-band {
    margin-top: 14px;
    width: 92px;
    height: 8px;
    background: linear-gradient(90deg, rgba(255,255,255,0.5), rgba(255,255,255,0.04));
  }

  /* Contact side */
  .card--contact { left: 620px; background: var(--brand-white); }
  .contact-layout {
    position: absolute;
    top: 86px;
    left: 26px;
    display: flex;
    align-items: center;
  }
  .card--contact .wordmark { font-size: 44px; color: var(--ink); margin-right: 12px; margin-top: 44px; }
  .card--contact .wordmark__dot { width: 18px; height: 18px; background: var(--brand-lilac); margin-top: 8px; }
  .contact-divider {
    width: 1px;
    height: 112px;
    background: var(--rule);
    margin-right: 12px;
  }
  .person__name {
    font-size: 15px;
    font-weight: 700;
    color: var(--brand-purple);
  }
  .person__role {
    font-size: 12.5px;
    color: var(--brand-lilac);
    margin-bottom: 8px;
  }
  .contact-list { list-style: none; }
  .contact-list li {
    display: flex;
    align-items: center;
    gap: 7px;
    font-size: 12.5px;
    color: var(--ink);
    line-height: 1.6;
    white-space: nowrap;
  }
  .contact-list svg { width: 11px; height: 11px; fill: var(--brand-purple); flex: none; }
  .contact-band {
    position: absolute;
    left: 120px;
    bottom: 36px;
    width: 386px;
    height: 14px;
    background: linear-gradient(90deg, rgba(107,68,155,0.05), var(--brand-purple) 47%, rgba(107,68,155,0.06));
  }
</style>
</head>
<body>
<main class="stage">

  <section class="card card--art" aria-label="Brightfen card, art side">
    <div class="card__backdrop" role="img" aria-label="Darkened, softly blurred photo of a suburban house"></div>
    <div class="card__content">
      <div class="wordmark"><span class="wordmark__dot"></span><span>brightfen</span></div>
      <p class="pitch">MOST people do not have access to any means of responding to Security alarms in MINUTES. Public Safety services won't attend to an alarm without visual confirmation that an event is real.</p>
      <p class="pitch__tagline">It's time for change. Introducing...</p>
      <div class="pitch-band" role="img" aria-label="Fading decorative band"></div>
    </div>
  </section>

  <section class="card card--contact" aria-label="Brightfen card, contact side">
    <div class="contact-layout">
      <div class="wordmark"><span class="wordmark__dot"></span><span>brightfen</span></div>
      <div class="contact-divider"></div>
      <div class="person">
        <p class="person__name">Dorian Felkatsis</p>
        <p class="person__role">Managing Director</p>
        <ul class="contact-list">
          <li>
            <svg viewBox="0 0 12 12" aria-hidden="true"><path d="M6 0a4 4 0 0 0-4 4c0 3 4 8 4 8s4-5 4-8a4 4 0 0 0-4-4zm0 5.6A1.6 1.6 0 1 1 6 2.4a1.6 1.6 0 0 1 0 3.2z"/></svg>
            47 Larkfield Avenue, Toronto, On, M6K2B7
          </li>
          <li>
            <svg viewBox="0 0 12 12" aria-hidden="true"><path d="M1 3.5C1 2 2.5 1 6 1s5 1 5 2.5V5H8.5V3.8h-5V5H1zM2.5 6h7l1 5h-9zM6 7.2a1.4 1.4 0 1 0 0 2.8 1.4 1.4 0 0 0 0-2.8z"/></svg>
            416-7291846
          </li>
          <li>
            <svg viewBox="0 0 12 12" aria-hidden="true"><path d="M0 2h12v1.2L6 7 0 3.2zM0 4.6l6 3.8 6-3.8V10H0z"/></svg>
            rolo@brightfen.io
          </li>
        </ul>
      </div>
    </div>
    <div class="contact-band" role="img" aria-label="Purple decorative band fading at both ends"></div>
  </section>

</main>
</body>
</html>
```